Copper Ridge Business Cards For New Startup

I am looking for you to design some business cards for a new startup https://copperridgehub.example. I have supplied logo, brand guidelines and our signatures as a guide.

We need this to reflect the brand guidelines and the website for brand consistency,

What is Copper Ridge?

Mallorca's Business Growth Community
Join your new business community full of passionate entrepreneurs who
love to solve problems and help each other grow together!

Any questions you can ask.

Target Market(s)

Business to Business

Contact Information for Business Card

These are attached (signatures) to the job

Font styles to use
Other font styles liked:
• Open Sans

Requirements
Must have
• Match design guidelines
Nice to have
• Photos of our faces so people remember us

```html
<!DOCTYPE html>
<html lang="en">
<head>
<meta charset="utf-8">
<title>Copper Ridge Business Cards</title>
<link href="https://fonts.googleapis.com/css2?family=Open+Sans:wght@400;600;700&display=swap" rel="stylesheet">
<style>
  :root {
    --stage: #3a3a3c;
    --olive: #666600;
    --olive-dark: #575700;
    --white: #ffffff;
    --band: rgba(255,255,255,0.9);
    --photo-top: #b8a08a;
    --photo-bottom: #6f86a6;
  }
  * { box-sizing: border-box; margin: 0; padding: 0; }
  html, body { width: 1200px; height: 1000px; overflow: hidden; }
  body {
    background: var(--stage);
    font-family: "Open Sans", sans-serif;
    color: var(--white);
    position: relative;
  }
  .card {
    position: absolute;
    left: 220px;
    width: 760px;
    height: 430px;
    background: var(--olive);
    border-radius: 26px;
    overflow: hidden;
    box-shadow: 0 10px 30px rgba(0,0,0,0.35);
  }
  .card--back { top: 50px; }
  .card--front { top: 520px; }

  .wordmark {
    font-weight: 600;
    letter-spacing: 1px;
    color: var(--white);
    white-space: nowrap;
  }
  .mark-circle {
    border: 3px solid var(--white);
    border-radius: 50%;
  }

  /* back */
  .back-logo {
    position: absolute;
    left: 50%; top: 50%;
    transform: translate(-50%, -50%);
    display: flex;
    align-items: center;
    gap: 34px;
  }
  .back-logo .mark-circle { width: 96px; height: 96px; }
  .back-logo .wordmark { font-size: 44px; }

  /* front */
  .portrait {
    position: absolute;
    left: 40px; top: 40px;
    width: 310px; height: 390px;
    border-radius: 150px 150px 0 0;
    background: linear-gradient(180deg, var(--photo-top) 0%, #c9b09a 45%, var(--photo-bottom) 100%);
  }
  .name-band {
    position: absolute;
    left: 0; bottom: 40px;
    width: 370px; height: 96px;
    background: linear-gradient(90deg, var(--band) 0%, var(--band) 75%, rgba(255,255,255,0) 100%);
    padding: 14px 0 0 30px;
  }
  .person-name {
    color: var(--olive);
    font-weight: 700;
    font-size: 28px;
    line-height: 1.1;
  }
  .person-role {
    color: var(--olive-dark);
    font-size: 15px;
    margin-top: 4px;
  }
  .brand-block {
    position: absolute;
    right: 60px; top: 36px;
    display: flex;
    flex-direction: column;
    align-items: center;
  }
  .brand-block .mark-circle { width: 150px; height: 150px; }
  .brand-block .wordmark { font-size: 38px; margin-top: 18px; }
  .contact-list {
    position: absolute;
    right: 48px; top: 265px;
    list-style: none;
    text-align: right;
  }
  .contact-list li {
    display: flex;
    justify-content: flex-end;
    align-items: center;
    gap: 10px;
    font-size: 20px;
    line-height: 29px;
  }
  .contact-list .web b { font-weight: 700; }
  .contact-list svg { width: 18px; height: 18px; flex: none; }
  .social-row {
    position: absolute;
    right: 48px; bottom: 32px;
    display: flex;
    gap: 12px;
  }
  .social-dot {
    width: 32px; height: 32px;
    border-radius: 50%;
    background: var(--olive-dark);
    border: 1px solid rgba(255,255,255,0.25);
  }
</style>
</head>
<body>

<section class="card card--back" aria-label="Business card back">
  <div class="back-logo">
    <div class="mark-circle"></div>
    <span class="wordmark">COPPER RIDGE</span>
  </div>
</section>

<section class="card card--front" aria-label="Business card front">
  <div class="portrait" role="img" aria-label="Portrait photo of Daniel Hartley, smiling, in a blue blazer"></div>
  <div class="name-band">
    <p class="person-name">Daniel Hartley</p>
    <p class="person-role">Founder &amp; Growth Hacker | Copper Ridge</p>
  </div>

  <div class="brand-block">
    <div class="mark-circle"></div>
    <span class="wordmark">COPPER RIDGE</span>
  </div>

  <ul class="contact-list">
    <li>+34 600 555 021
      <svg viewBox="0 0 24 24" fill="none" stroke="#fff" stroke-width="2"><path d="M5 3h4l2 5-2.5 1.5a11 11 0 0 0 6 6L16 13l5 2v4a2 2 0 0 1-2 2A16 16 0 0 1 3 5a2 2 0 0 1 2-2z"/></svg>
    </li>
    <li>dh@copperridgehub.example
      <svg viewBox="0 0 24 24" fill="none" stroke="#fff" stroke-width="2"><rect x="3" y="5" width="18" height="14" rx="1"/><polyline points="3,6 12,13 21,6"/></svg>
    </li>
    <li class="web"><span><b>copperridgehub</b>.example</span>
      <svg viewBox="0 0 24 24" fill="none" stroke="#fff" stroke-width="2"><circle cx="12" cy="12" r="9"/><ellipse cx="12" cy="12" rx="4" ry="9"/><line x1="3" y1="12" x2="21" y2="12"/></svg>
    </li>
  </ul>

  <div class="social-row" aria-label="Social media links">
    <span class="social-dot"></span>
    <span class="social-dot"></span>
    <span class="social-dot"></span>
    <span class="social-dot"></span>
    <span class="social-dot"></span>
  </div>
</section>

</body>
</html>
```